Flyer for customer acquisition.

Hello, We are a sportmanagement agency from Germany and we need information flyers for customer acquisition. It should be DinA4 and should have a modern but serious design. I have uploaded a information sheet, where you can find the text and the composition, the flyer should have. I also uploaded Pictures / Images, which you can use. Of course you can use other suitable images. If they are not free, I will buy them later. On the bottom of the flyer there has been the contact information. You will find them in the download section, too. If you have questions, just write me. If I forgot something, I will update the letter :) Thank you very much!
Ich brauche zusätzliche Tage um durchzusehen

```html
<!DOCTYPE html>
<html lang="de">
<head>
<meta charset="utf-8">
<title>KORVA Nachwuchsförderung – Flyer</title>
<link href="https://fonts.googleapis.com/css2?family=Montserrat:wght@400;500;700;800&family=Oswald:wght@600;700&display=swap" rel="stylesheet">
<style>
  :root{
    --page-bg:#e6e6e6;
    --icon-green:#1f5a2b;
    --title-green-top:#3c6a2c;
    --title-green-bottom:#0e2a12;
    --ink:#141a14;
    --white:#ffffff;
    --band-black:#0b0d0a;
    --accent-lime:#c7d64a;
    --sky-grey:#8d927c;
    --haze:#f5f8e4;
    --pitch:#7db43a;
    --pitch-dark:#1d3a10;
  }
  *{box-sizing:border-box;margin:0;padding:0}
  html,body{width:994px;height:1200px;overflow:hidden;background:var(--page-bg)}
  .flyer{position:absolute;left:73px;top:0;width:848px;height:1200px;overflow:hidden;
    font-family:"Montserrat",Arial,sans-serif;color:var(--ink)}
  .stadium-photo{position:absolute;inset:0;
    background:
      radial-gradient(ellipse 70% 38% at 50% 52%, rgba(255,255,240,.95), rgba(255,255,240,0) 70%),
      linear-gradient(180deg,var(--sky-grey) 0%,#c9cdb4 14%,var(--haze) 40%,#e9f1c8 55%,#a8cf63 70%,var(--pitch) 82%,var(--pitch-dark) 100%)}
  .brand{position:absolute;left:40px;top:60px;width:246px;display:flex;align-items:center;justify-content:center;gap:12px}
  .brand-dot{width:26px;height:26px;border-radius:50%;background:#2a2e28}
  .brand-name{font-weight:700;font-size:40px;color:#2a2e28;letter-spacing:1px}
  .headline{position:absolute;left:304px;top:22px;width:512px;text-align:center;font-family:"Oswald",sans-serif;white-space:nowrap}
  .headline-top{font-weight:700;font-size:34px;line-height:44px;color:var(--white);
    text-shadow:0 2px 3px rgba(0,0,0,.7)}
  .headline-main{font-weight:700;font-size:62px;line-height:70px;letter-spacing:1px;
    background:linear-gradient(180deg,var(--title-green-top),var(--title-green-bottom));
    -webkit-background-clip:text;background-clip:text;color:transparent;
    filter:drop-shadow(0 2px 1px rgba(255,255,255,.6))}
  .tagline{position:absolute;left:314px;top:143px;width:492px;height:22px;background:var(--band-black);
    color:var(--white);font-weight:700;font-size:11.5px;letter-spacing:2px;text-align:center;line-height:20px;
    border:1px solid #6b6b6b;white-space:nowrap}
  .service{position:absolute;left:78px;width:570px}
  .service-tick{position:absolute;left:0;top:1px;width:19px;height:19px}
  .service-title{margin-left:26px;font-weight:800;font-size:19px;line-height:22px;text-transform:uppercase;letter-spacing:.3px;white-space:nowrap}
  .service-text{margin-left:26px;font-weight:500;font-size:15px;line-height:21.5px;white-space:nowrap}
  .service-icon{position:absolute;left:680px;width:82px;height:82px}
  .chess-silhouettes{position:absolute;left:111px;top:850px;width:556px;height:175px;
    background:linear-gradient(180deg,rgba(90,170,60,.55),rgba(50,130,40,.85));
    border-radius:40px 40px 6px 6px}
  .player-illustration{position:absolute;left:650px;top:680px;width:198px;height:370px;
    background:linear-gradient(160deg,#2a6db8 0%,#b22a86 35%,#f09a2c 70%,#f4f1e0 100%);
    border-radius:90px 90px 20px 20px;opacity:.9}
  .footnote{position:absolute;left:48px;top:1040px;width:756px;height:72px;background:var(--band-black);
    clip-path:polygon(4% 0,100% 0,96% 100%,0 100%);color:var(--white);text-align:center;
    font-weight:700;font-size:9.5px;line-height:13px;padding:12px 44px 0}
  .footnote p+p{margin-top:8px}
  .contact{position:absolute;left:0;top:1122px;width:848px;display:flex;justify-content:center;gap:38px;align-items:center}
  .contact-item{display:flex;align-items:center;gap:10px;color:var(--white);font-weight:500;font-size:19px;
    text-shadow:0 1px 2px rgba(0,0,0,.6);white-space:nowrap}
  .contact-icon{width:26px;height:26px;border-radius:50%;background:var(--accent-lime);display:flex;align-items:center;justify-content:center}
</style>
</head>
<body>
<div class="flyer">
  <div class="stadium-photo" role="img" aria-label="Foto eines Fußballstadions mit bewölktem Himmel, Flutlicht und grünem Rasen"></div>

  <div class="brand"><span class="brand-dot"></span><span class="brand-name">KORVA</span></div>

  <div class="headline">
    <div class="headline-top">KORVA NACHWUCHSFÖRDERUNG</div>
    <div class="headline-main">UND -MANGEMENT</div>
  </div>
  <div class="tagline">WIR BEGLEITEN DICH AUF DEINEM WEG ZUM PROFI!</div>

  <svg width="0" height="0" style="position:absolute">
    <defs>
      <symbol id="tick" viewBox="0 0 20 20"><circle cx="10" cy="10" r="10" fill="#1f5a2b"/><path d="M5.5 10.5l3 3 6-6.5" fill="none" stroke="#fff" stroke-width="2.4" stroke-linecap="round" stroke-linejoin="round"/></symbol>
    </defs>
  </svg>

  <div class="service" style="top:206px">
    <svg class="service-tick"><use href="#tick"/></svg>
    <div class="service-title">Karriereplanung</div>
    <div class="service-text">Wir haben deine Karriere im Blick! In enger Absprache mit deinen<br>Eltern und dir leiten wir die richtigen Maßnahmen und Schritte ein,<br>um dein Ziel „Profifußballer“ zu realisieren.</div>
  </div>
  <div class="service" style="top:315px">
    <svg class="service-tick"><use href="#tick"/></svg>
    <div class="service-title">Ständiger Ansprechpartner</div>
    <div class="service-text">Egal um welchen Themen es sich handelt, wir sind für dich da!<br>Ein vertrauensvolles und freundschaftliches Verhältnis ist uns<br>besonders wichtig.</div>
  </div>
  <div class="service" style="top:423px">
    <svg class="service-tick"><use href="#tick"/></svg>
    <div class="service-title">Rechtsberatung/Vertragsrecht</div>
    <div class="service-text">Juristendeutsch und Kleingedrucktes? Kein Problem! Wir helfen<br>dir den Durchblick zu behalten und holen immer das Beste für dich<br>raus.</div>
  </div>
  <div class="service" style="top:527px">
    <svg class="service-tick"><use href="#tick"/></svg>
    <div class="service-title">Ausrüstung</div>
    <div class="service-text">Wir besorgen dir deine Ausrüstung! Unsere Beziehungen zu den<br>großen Sportartikelherstellern ermöglichen den Abschluss von<br>Ausrüsterverträgen*.</div>
  </div>
  <div class="service" style="top:632px">
    <svg class="service-tick"><use href="#tick"/></svg>
    <div class="service-title">Vorsorge</div>
    <div class="service-text">Verletzungen gehören leider zum Fußball dazu. Wir sichern dich<br>ab, indem wir eine private Zusatzkrankenversicherung für dich<br>abschließen.</div>
  </div>
  <div class="service" style="top:740px">
    <svg class="service-tick"><use href="#tick"/></svg>
    <div class="service-title">Kooperationspartner /Netzwerk</div>
    <div class="service-text">Ob Entscheidungsträger oder Experte, wir kennen<br>die richtigen Leute. Zusätzlich bieten wir dir eine große<br>Bandbreite an Leistungen, die du jederzeit in Anspruch<br>nehmen kannst**.</div>
  </div>

  <svg class="service-icon" style="top:200px" viewBox="0 0 80 80" fill="#1f5a2b">
    <circle cx="22" cy="12" r="6"/>
    <path d="M16 22h10l4 14h-6v20h-6V38l-6 8-4-4z"/>
    <path d="M6 74h18V62h14V50h14V38h14v-8h8v14H58v12H44v12H30v12H6z"/>
  </svg>
  <svg class="service-icon" style="top:296px" viewBox="0 0 80 80" fill="none" stroke="#1f5a2b" stroke-width="4">
    <path d="M10 14c4-4 8-4 10 0l5 8c2 3 0 6-3 8 2 6 7 11 13 14" fill="#1f5a2b" stroke-linejoin="round"/>
    <rect x="34" y="26" width="40" height="28" rx="2"/>
    <path d="M34 28l20 16 20-16"/>
    <circle cx="48" cy="66" r="7"/><path d="M55 66v3a3 3 0 0 0 6 0v-3a13 13 0 1 0-5 10"/>
  </svg>
  <svg class="service-icon" style="top:396px" viewBox="0 0 80 80" fill="none" stroke="#1f5a2b" stroke-width="4" stroke-linecap="round">
    <path d="M40 8v60M22 70h36M14 20h52"/>
    <path d="M14 20L5 42h18zM66 20l-9 22h18z" stroke-linejoin="round"/>
    <path d="M5 42a9 6 0 0 0 18 0M57 42a9 6 0 0 0 18 0" fill="#1f5a2b"/>
  </svg>
  <svg class="service-icon" style="top:500px" viewBox="0 0 80 80" fill="#1f5a2b">
    <path d="M46 10h8l2 8 7 3 7-5 6 6-5 7 3 7 8 2v8l-8 2-3 7 5 7-6 6-7-5-7 3-2 8h-8l-2-8-5-2 4-10a12 12 0 1 0 0-22l-4-10 5-2z"/>
    <path d="M10 14l8-4 10 10-3 5 22 22 5-3 10 10-4 8-12-12-6 2-26-26 2-6z"/>
  </svg>
  <svg class="service-icon" style="top:609px" viewBox="0 0 80 80">
    <circle cx="40" cy="40" r="35" fill="none" stroke="#1f5a2b" stroke-width="5"/>
    <path d="M30 26a3 3 0 0 1 6 0v14V20a3 3 0 0 1 6 0v20V22a3 3 0 0 1 6 0v20-12a3 3 0 0 1 6 0v22c0 8-6 14-13 14s-11-4-13-9l-6-13a3 3 0 0 1 5-3l3 5z" fill="#1f5a2b"/>
  </svg>
  <svg style="position:absolute;left:566px;top:727px;width:78px;height:78px" viewBox="0 0 80 80" fill="#1f5a2b" stroke="#1f5a2b" stroke-width="4">
    <path d="M40 40L16 14M40 40L66 14M40 40L10 52M40 40L70 52M40 40V70"/>
    <circle cx="40" cy="40" r="12"/><circle cx="16" cy="14" r="8"/><circle cx="66" cy="14" r="8"/>
    <circle cx="10" cy="52" r="7"/><circle cx="70" cy="52" r="7"/><circle cx="40" cy="70" r="7"/>
  </svg>

  <div class="chess-silhouettes" role="img" aria-label="Reihe grüner Schachfiguren-Silhouetten mit Rasentextur"></div>
  <div class="player-illustration" role="img" aria-label="Farbenfrohe Illustration eines Fußballspielers mit Ball und Farbspritzern"></div>

  <div class="footnote">
    <p>*Die Entscheidung über das Zustandekommen eines Ausrüstervertrags obliegt dem jeweiligen Sportartikelhersteller. Ist ein Abschluss aktuell nicht möglich, erhältst du von uns 2x pro Saison neue Fußballschuhe sowie weitere Ausrüstungsgegenstände.</p>
    <p>**Personal Training, Athletik-Training, Ernährungsberatung, Sportpsychologische Betreuung, uvm.</p>
  </div>

  <div class="contact">
    <div class="contact-item">
      <span class="contact-icon"><svg width="15" height="15" viewBox="0 0 20 20"><path d="M4 2l3 0 2 5-2 2c1 2 3 4 5 5l2-2 5 2v3c0 1-1 2-2 2C9 19 1 11 1 4c0-1 1-2 3-2z" fill="#1c2b10"/></svg></span>
      07000/4418250
    </div>
    <div class="contact-item">
      <span class="contact-icon"><svg width="15" height="15" viewBox="0 0 20 20"><rect x="1" y="4" width="18" height="12" fill="#1c2b10"/><path d="M1 4l9 7 9-7" fill="none" stroke="#c7d64a" stroke-width="1.6"/></svg></span>
      info@korva-sport.de
    </div>
    <div class="contact-item">
      <span class="contact-icon"><svg width="18" height="10" viewBox="0 0 24 10"><text x="12" y="8" text-anchor="middle" font-family="Montserrat,sans-serif" font-size="8" font-weight="700" fill="#1c2b10">www</text></svg></span>
      www.korva-sport.de
    </div>
  </div>
</div>
</body>
</html>
```